Speisekarten für ein modernes, junges Café
Zielgruppe
Wir suchen eine Speisekarte für ein modernes, junges Café. Frühstück, kleine Speisen, Snacks und Getränke stehen auf der Karte. Unsere Zielgruppe sind hauptsächlich junge Menschen bis 40 Jahre.
Die Speisekarte sollte immer änderbar sein ( nur Text bei neuen Speisen zum Beispiel )
Aufgabenstellung
Das Logo kann und soll gerne mit eingefügt werden. Eventuell gleich auf dem Deckblatt.
Generell bin ich offen für junge, coole Ideen.
Unten die Themen/ grobe Überschriften
Kaffee und Espresso
Frühstücksvariationen
Eierspeisen
Frühstück zum löffeln
Pancakes
Extras zum Frühstück
Snacks/ kleine Speisen
-die Kurbel. Drinks
-die Kurbel. Wein & Bier )
((Kinderspeisekarte:
zusätzlich noch ein extra Blatt für die Kinder zum ausmalen mit den illustrierten Bildern auch im modernen Stil ))

```html
<!DOCTYPE html>
<html lang="en">
<head>
<meta charset="utf-8">
<title>die Kurbel. – Café &amp; Bar Menu</title>
<link rel="stylesheet" href="https://fonts.googleapis.com/css2?family=Bebas+Neue&family=Montserrat:wght@400;700&display=swap">
<style>
  :root {
    --backdrop: #c6c6c6;
    --ink: #231f20;
    --paper: #ffffff;
    --sand: #d4c3a5;
    --sand-light: #f5eadf;
    --sand-rule: #cfb38f;
    --gold-hi: #f4ece0;
  }
  * { box-sizing: border-box; margin: 0; padding: 0; }
  html, body { width: 1200px; height: 1117px; overflow: hidden; }
  body { background: var(--backdrop); position: relative; font-family: "Montserrat", sans-serif; color: var(--ink); }

  .page { position: absolute; top: 180px; width: 536px; height: 757px; overflow: hidden; background: var(--paper); }
  .page--main { left: 53px; }
  .page--kids { left: 611px; background: var(--sand); }
  .page-shapes { position: absolute; inset: 0; width: 100%; height: 100%; }

  .brand { position: absolute; left: 30px; top: 0; width: 150px; height: 150px; border-radius: 50%; background: var(--paper); display: flex; flex-direction: column; align-items: center; justify-content: center; }
  .brand-name { font-family: "Montserrat", sans-serif; font-weight: 700; font-size: 19px; color: var(--ink); line-height: 1.2; text-align: center; }

  .section { position: absolute; }
  .section-title { font-family: "Bebas Neue", sans-serif; font-size: 22px; line-height: 1; letter-spacing: 0.2px; color: var(--ink); margin-bottom: 8px; }
  .item { height: 22.6px; }
  .item-name { font-weight: 700; font-size: 11px; line-height: 12px; }
  .item-desc { font-size: 7.6px; line-height: 10px; white-space: nowrap; }
  .rule { position: absolute; height: 1px; background: var(--sand-rule); }

  .banner { position: absolute; text-align: center; color: var(--paper); }
  .banner-title { font-family: "Bebas Neue", sans-serif; font-size: 20px; line-height: 1; }
  .banner-sub { font-weight: 700; font-size: 8.5px; line-height: 1.1; }

  .drinks-box { position: absolute; left: 39px; top: 576px; width: 458px; height: 152px; background: var(--paper); }
  .drinks-frame { position: absolute; inset: 5px; border: 1px solid #9a9a9a; }

  .kids-inner { position: absolute; left: 16px; top: 16px; width: 504px; height: 726px; background: var(--paper); }
  .kids-rule { position: absolute; left: 52px; top: 182px; width: 432px; height: 2px; background: var(--ink); }
  .coloring-sheet { position: absolute; left: 28px; top: 218px; width: 453px; height: 492px; }
</style>
</head>
<body>

<!-- Main menu page -->
<section class="page page--main" aria-label="Breakfast menu">
  <svg class="page-shapes" viewBox="0 0 536 757" aria-hidden="false">
    <defs>
      <linearGradient id="photoTone" x1="0" y1="0" x2="1" y2="1">
        <stop offset="0" stop-color="#e9e4dc"/>
        <stop offset="0.45" stop-color="#d9a679"/>
        <stop offset="0.75" stop-color="#b9c08a"/>
        <stop offset="1" stop-color="#c7c2bd"/>
      </linearGradient>
      <linearGradient id="goldBand" x1="0" y1="0" x2="0" y2="1">
        <stop offset="0" stop-color="var(--sand)"/>
        <stop offset="0.5" stop-color="var(--gold-hi)"/>
        <stop offset="1" stop-color="var(--sand)"/>
      </linearGradient>
    </defs>
    <rect x="0" y="134" width="16" height="520" fill="url(#goldBand)"/>
    <rect x="519" y="232" width="17" height="640" fill="url(#goldBand)"/>
    <polygon points="0,597 536,696 536,757 0,757" fill="var(--ink)"/>
    <polygon points="0,0 536,0 536,238 0,134" fill="url(#photoTone)" role="img" aria-label="Photo of a breakfast table with croissants, strawberries, orange juice, muesli bowls, coffee and kiwi"/>
    <polygon points="255,183 497,228 497,496 255,496" fill="var(--sand-light)"/>
    <path d="M275,503 H477 C460,545 420,562 376,562 C332,562 292,545 275,503 Z" fill="var(--ink)"/>
  </svg>

  <div class="brand"><span class="brand-name">die Kurbel.</span></div>

  <div class="section" style="left:39px; top:165px;">
    <h2 class="section-title">Coffee and Espresso</h2>
    <div class="item"><p class="item-name">Lorem ipsum</p><p class="item-desc">Lorem ipsum dolor sit amet, consectetur adipiscing elit,</p></div>
    <div class="item"><p class="item-name">Lorem ipsum</p><p class="item-desc">Lorem ipsum dolor sit amet, consectetur adipiscing elit,</p></div>
    <div class="item"><p class="item-name">Lorem ipsum</p><p class="item-desc">Lorem ipsum dolor sit amet, consectetur adipiscing elit,</p></div>
    <div class="item"><p class="item-name">Lorem ipsum</p><p class="item-desc">Lorem ipsum dolor sit amet, consectetur adipiscing elit,</p></div>
  </div>
  <div class="rule" style="left:39px; top:291px; width:192px;"></div>

  <div class="section" style="left:39px; top:306px;">
    <h2 class="section-title">Egg Dishes</h2>
    <div class="item"><p class="item-name">Lorem ipsum</p><p class="item-desc">Lorem ipsum dolor sit amet, consectetur adipiscing elit,</p></div>
    <div class="item"><p class="item-name">Lorem ipsum</p><p class="item-desc">Lorem ipsum dolor sit amet, consectetur adipiscing elit,</p></div>
    <div class="item"><p class="item-name">Lorem ipsum</p><p class="item-desc">Lorem ipsum dolor sit amet, consectetur adipiscing elit,</p></div>
    <div class="item"><p class="item-name">Lorem ipsum</p><p class="item-desc">Lorem ipsum dolor sit amet, consectetur adipiscing elit,</p></div>
  </div>
  <div class="rule" style="left:39px; top:433px; width:192px;"></div>

  <div class="section" style="left:39px; top:447px;">
    <h2 class="section-title">Pancakes</h2>
    <div class="item"><p class="item-name">Lorem ipsum</p><p class="item-desc">Lorem ipsum dolor sit amet, consectetur adipiscing elit,</p></div>
    <div class="item"><p class="item-name">Lorem ipsum</p><p class="item-desc">Lorem ipsum dolor sit amet, consectetur adipiscing elit,</p></div>
    <div class="item"><p class="item-name">Lorem ipsum</p><p class="item-desc">Lorem ipsum dolor sit amet, consectetur adipiscing elit,</p></div>
    <div class="item"><p class="item-name">Lorem ipsum</p><p class="item-desc">Lorem ipsum dolor sit amet, consectetur adipiscing elit,</p></div>
  </div>

  <div class="section" style="left:278px; top:225px;">
    <h2 class="section-title">Breakfast Variations</h2>
    <div class="item"><p class="item-name">Lorem ipsum</p><p class="item-desc">Lorem ipsum dolor sit amet, consectetur adipiscing elit,</p></div>
    <div class="item"><p class="item-name">Lorem ipsum</p><p class="item-desc">Lorem ipsum dolor sit amet, consectetur adipiscing elit,</p></div>
    <div class="item"><p class="item-name">Lorem ipsum</p><p class="item-desc">Lorem ipsum dolor sit amet, consectetur adipiscing elit,</p></div>
    <div class="item"><p class="item-name">Lorem ipsum</p><p class="item-desc">Lorem ipsum dolor sit amet, consectetur adipiscing elit,</p></div>
  </div>
  <div class="rule" style="left:278px; top:352px; width:192px;"></div>

  <div class="section" style="left:278px; top:366px;">
    <h2 class="section-title">Breakfast to Eat</h2>
    <div class="item"><p class="item-name">Lorem ipsum</p><p class="item-desc">Lorem ipsum dolor sit amet, consectetur adipiscing elit,</p></div>
    <div class="item"><p class="item-name">Lorem ipsum</p><p class="item-desc">Lorem ipsum dolor sit amet, consectetur adipiscing elit,</p></div>
    <div class="item"><p class="item-name">Lorem ipsum</p><p class="item-desc">Lorem ipsum dolor sit amet, consectetur adipiscing elit,</p></div>
    <div class="item"><p class="item-name">Lorem ipsum</p><p class="item-desc">Lorem ipsum dolor sit amet, consectetur adipiscing elit,</p></div>
  </div>

  <div class="banner" style="left:275px; top:516px; width:202px;">
    <p class="banner-title">Extras for Breakfast</p>
    <p class="banner-sub">Snacks/small dishes</p>
  </div>

  <div class="drinks-box">
    <div class="drinks-frame"></div>
    <div class="section" style="left:20px; top:15px;">
      <h2 class="section-title">Drinks</h2>
      <div class="item"><p class="item-name">Lorem ipsum</p><p class="item-desc">Lorem ipsum dolor sit amet, consectetur adipiscing elit,</p></div>
      <div class="item"><p class="item-name">Lorem ipsum</p><p class="item-desc">Lorem ipsum dolor sit amet, consectetur adipiscing elit,</p></div>
      <div class="item"><p class="item-name">Lorem ipsum</p><p class="item-desc">Lorem ipsum dolor sit amet, consectetur adipiscing elit,</p></div>
      <div class="item"><p class="item-name">Lorem ipsum</p><p class="item-desc">Lorem ipsum dolor sit amet, consectetur adipiscing elit,</p></div>
    </div>
    <div class="section" style="left:244px; top:15px;">
      <h2 class="section-title">Wine &amp; Beer</h2>
      <div class="item"><p class="item-name">Lorem ipsum</p><p class="item-desc">Lorem ipsum dolor sit amet, consectetur adipiscing elit,</p></div>
      <div class="item"><p class="item-name">Lorem ipsum</p><p class="item-desc">Lorem ipsum dolor sit amet, consectetur adipiscing elit,</p></div>
      <div class="item"><p class="item-name">Lorem ipsum</p><p class="item-desc">Lorem ipsum dolor sit amet, consectetur adipiscing elit,</p></div>
      <div class="item"><p class="item-name">Lorem ipsum</p><p class="item-desc">Lorem ipsum dolor sit amet, consectetur adipiscing elit,</p></div>
    </div>
  </div>
</section>

<!-- Children's menu page -->
<section class="page page--kids" aria-label="Children's menu">
  <svg class="page-shapes" viewBox="0 0 536 757" aria-hidden="true">
    <defs>
      <linearGradient id="goldBandKids" x1="0" y1="0" x2="0" y2="1">
        <stop offset="0" stop-color="var(--sand)"/>
        <stop offset="0.5" stop-color="var(--gold-hi)"/>
        <stop offset="1" stop-color="var(--sand)"/>
      </linearGradient>
    </defs>
    <rect x="0" y="0" width="536" height="757" fill="url(#goldBandKids)"/>
    <polygon points="0,597 536,696 536,757 0,757" fill="var(--ink)"/>
  </svg>

  <div class="kids-inner">
    <svg class="page-shapes" viewBox="0 0 504 726" aria-hidden="true">
      <path d="M135,-16 H369 C350,20 300,42 252,42 C204,42 154,20 135,-16 Z" fill="var(--ink)"/>
    </svg>
    <div class="banner" style="left:135px; top:2px; width:234px;">
      <p class="banner-title">Children's Menu:</p>
    </div>

    <div class="section" style="left:37px; top:59px;">
      <div class="item"><p class="item-name">Lorem ipsum</p><p class="item-desc">Lorem ipsum dolor sit amet, consectetur adipiscing elit,</p></div>
      <div class="item"><p class="item-name">Lorem ipsum</p><p class="item-desc">Lorem ipsum dolor sit amet, consectetur adipiscing elit,</p></div>
      <div class="item"><p class="item-name">Lorem ipsum</p><p class="item-desc">Lorem ipsum dolor sit amet, consectetur adipiscing elit,</p></div>
      <div class="item"><p class="item-name">Lorem ipsum</p><p class="item-desc">Lorem ipsum dolor sit amet, consectetur adipiscing elit,</p></div>
    </div>
    <div class="section" style="left:269px; top:59px;">
      <div class="item"><p class="item-name">Lorem ipsum</p><p class="item-desc">Lorem ipsum dolor sit amet, consectetur adipiscing elit,</p></div>
      <div class="item"><p class="item-name">Lorem ipsum</p><p class="item-desc">Lorem ipsum dolor sit amet, consectetur adipiscing elit,</p></div>
      <div class="item"><p class="item-name">Lorem ipsum</p><p class="item-desc">Lorem ipsum dolor sit amet, consectetur adipiscing elit,</p></div>
      <div class="item"><p class="item-name">Lorem ipsum</p><p class="item-desc">Lorem ipsum dolor sit amet, consectetur adipiscing elit,</p></div>
    </div>

    <div class="kids-rule"></div>

    <svg class="coloring-sheet" viewBox="0 0 453 492" role="img" aria-label="Colouring page illustration: 'Happy Coloring' lettering with a pineapple, an ice lolly, a cake, a strawberry, an apple and stars in black outlines">
      <defs>
        <linearGradient id="sheetTone" x1="0" y1="0" x2="0" y2="1">
          <stop offset="0" stop-color="#f4f2ef"/>
          <stop offset="1" stop-color="#e6e2dc"/>
        </linearGradient>
      </defs>
      <rect width="453" height="492" rx="6" fill="url(#sheetTone)"/>
    </svg>
  </div>
</section>

</body>
</html>
```